Vibrant Spiritual Community Needs an Invitation Design

Millbrook Fellowship Church excels at helping the spiritually curious find answers to life's big questions. From Sept 15-Oct 27 our Sunday morning service will be focusing on the Seven Deadly Sins. Our approach is that the "sin" is the result of a God given urge being channeled in the wrong direction. The solution for "sin" then, is not repression but a re-channeling of the urge in a more profitable direction. Example: Beneath the sin of pride is the God given urge for power. Nothing wrong with the desire for power, but it needs to be channeled in the direction of empowering others or it becomes pride. For each sin, there is a corresponding energy and an appropriate channelling. The final design should be initially eye catching and stoke curiosity enough that someone who has never been to church decides to attend.

Target Market(s)

30-40 year old with young families who do not currently attend church.

Industry/Entity Type

Church

Requirements
Must have
• Must have the time the service starts and location of church.
(11am / 4812 Corran Rd East)
Must have a link to the website
(www.millbrookchapel.org)
Must mention MFCYouthGlow as a safe program for children.
(our program for children birth to grade 6 which runs during the Sunday service in a different part of the building. All volunteers trained and criminal record checked)
Nice to have
• A positive spin! Weird when we are talking about sin, but that is where the curiosity might come in. The message is ultimately positive. That we don't have to repress our urges and become less than human; we can re - channel them and become a new kind of human.

```html
<!DOCTYPE html>
<html lang="en">
<head>
<meta charset="utf-8">
<title>Millbrook Fellowship Church – Sunday Series Invitation</title>
<link rel="stylesheet" href="https://fonts.googleapis.com/css2?family=Anton&family=Krona+One&display=swap">
<style>
  :root {
    --maroon: #8c1422;
    --maroon-soft: #d9a9ae;
    --ink: #0c0c0c;
    --slate: #3a3a3a;
    --paper: #ffffff;
    --frame: #222222;
  }
  * { margin: 0; padding: 0; box-sizing: border-box; }
  html, body { width: 1200px; height: 828px; overflow: hidden; background: var(--paper); }
  .invitation {
    position: relative;
    width: 1200px;
    height: 828px;
    overflow: hidden;
    background: var(--paper);
    font-family: "Anton", "Arial Narrow", sans-serif;
    color: var(--ink);
  }
  .backdrop-art {
    position: absolute;
    inset: 0;
    background:
      linear-gradient(180deg, rgba(255,255,255,0) 0%, rgba(255,255,255,0) 88%, rgba(140,20,34,0.55) 100%),
      linear-gradient(90deg, #1b1b1b 0%, #3b3b3b 22%, #8c5a60 42%, var(--maroon-soft) 62%, #efe4e5 82%, #c9c9c9 100%);
  }
  .panel {
    position: absolute;
    left: 42px; top: 67px;
    width: 1106px; height: 683px;
    border: 1px solid var(--frame);
    background: linear-gradient(90deg,
      rgba(255,255,255,0.45) 0%,
      rgba(255,255,255,0.7) 30%,
      rgba(255,255,255,0.9) 55%,
      rgba(255,255,255,0.95) 100%);
  }
  .headline {
    position: absolute;
    left: 84px; top: 90px;
    font-family: "Krona One", "Arial Black", sans-serif;
    font-size: 80px;
    line-height: 1;
    letter-spacing: 20px;
    white-space: nowrap;
    color: var(--maroon);
    -webkit-text-stroke: 3px var(--ink);
    paint-order: stroke fill;
    transform-origin: left top;
    transform: scale(1.18, 1.02);
  }
  .series-intro {
    position: absolute;
    right: 75px; top: 203px;
    width: 900px;
    font-size: 28px;
    line-height: 45px;
    text-align: right;
  }
  .series-intro span { display: block; white-space: nowrap; }
  .church-name {
    position: absolute;
    left: 110px; top: 508px;
    display: flex; align-items: center; gap: 40px;
    font-size: 36px;
    line-height: 1.05;
    color: var(--slate);
  }
  .church-name .mark {
    width: 62px; height: 62px; border-radius: 50%;
    background: var(--slate); flex: none;
  }
  .address {
    position: absolute;
    left: 59px; top: 597px;
    font-size: 33px;
    line-height: 49px;
    font-style: normal;
  }
  .address span { display: block; white-space: nowrap; }
  .visit-details {
    position: absolute;
    right: 75px; top: 491px;
    width: 560px;
    font-size: 27px;
    line-height: 40.3px;
    text-align: right;
  }
  .visit-details span { display: block; white-space: nowrap; }
</style>
</head>
<body>
<main class="invitation">
  <div class="backdrop-art" role="img" aria-label="Oversized outlined SINS lettering in black and maroon behind the invitation"></div>

  <section class="panel"></section>

  <h1 class="headline">Your Invited!</h1>

  <p class="series-intro">
    <span>Join us Sundays Sept. 15 to Oct 27 at 10:30AM as we take a</span>
    <span>Positive spin on the 7 deadly Sins. The solution for "sin" is not</span>
    <span>repression but a re-channeling of the urge in a more positive</span>
    <span>direction. For each sin, there is a corresponding energy. We will</span>
    <span>learn we don't have to repress our urges and become less than</span>
    <span>human; we can re - channel them and become a new kind of</span>
  </p>

  <div class="church-name">
    <span class="mark"></span>
    <span>Millbrook Fellowship<br>Church</span>
  </div>

  <address class="address">
    <span>4812 Corran Rd East</span>
    <span>Millbrook, Manitoba R0K 4T2</span>
    <span>www.millbrookchapel.org</span>
  </address>

  <p class="visit-details">
    <span>Coffee is on at 10:30....come have a cup</span>
    <span>and visit before the Sunday service</span>
    <span>starts at 11AM.</span>
    <span>If you have kids age newborn to Grade</span>
    <span>6, allow a few minutes to get them</span>
    <span>signed into MFCYouthGlow.</span>
  </p>
</main>
</body>
</html>
```